Cedar Ridge Strong Partners and Households Initiative-Teen

We need a flyer that invites high school students to our program. The students go through healthy relationship education, financial stability and workforce readiness.

We are in five locations, so we need a flyer that we can edit the text to update addresses, dates and any additional information based on our needs.

Attached are the two logo's we would like to use. I have also attached a previous flyer that we created to give you an idea of the text that is included.

In the past we have only promoted the healthy relationship component, but if you are able to incorporate finances (money) and job development (jobs), that would be great.

Industry/Entity Type

School

Requirements
Must have
• Targets high school students
• Make the text available for us to edit
• Our topics is healthy relationship, money and jobs

```html
<!DOCTYPE html>
<html lang="en">
<head>
<meta charset="utf-8">
<title>H.E.A.R.T. talk for TEENS</title>
<link href="https://fonts.googleapis.com/css2?family=Overlock:wght@700;900&family=Pathway+Gothic+One&display=swap" rel="stylesheet">
<style>
  :root {
    --pink: #cc3360;
    --orange: #f39223;
    --blue: #1d4f91;
    --ink: #231f20;
    --white: #ffffff;
    --photo-warm: #b89a83;
    --photo-green: #7f9a5c;
    --photo-grey: #c9c3c0;
  }
  * { margin: 0; padding: 0; box-sizing: border-box; }
  html, body { width: 934px; height: 1200px; overflow: hidden; background: var(--white); }
  .flyer { position: relative; width: 934px; height: 1200px; background: var(--white); font-family: "Pathway Gothic One", "Arial Narrow", sans-serif; color: var(--ink); }
  .top-band { position: absolute; left: 0; top: 0; width: 934px; height: 68px; background: var(--pink); }
  .photo-strip { position: absolute; left: 0; top: 83px; }
  .divider { position: absolute; top: 358px; height: 12px; }
  .divider--pink { left: 0; width: 276px; background: var(--pink); }
  .divider--blue { left: 276px; width: 658px; background: var(--blue); }
  .title-band { position: absolute; left: 0; top: 376px; width: 934px; height: 266px; background: var(--orange); color: var(--white); padding: 82px 0 0 60px; }
  .title { font-family: "Overlock", "Trebuchet MS", sans-serif; font-weight: 900; font-size: 66px; line-height: 1; letter-spacing: 0.5px; }
  .subtitle { margin-top: 18px; font-size: 27px; line-height: 36px; letter-spacing: 1.2px; }
  .details-band { position: absolute; left: 0; top: 642px; width: 934px; height: 148px; background: var(--pink); color: var(--white); padding: 16px 0 0 60px; font-size: 21px; letter-spacing: 1.2px; line-height: 29px; }
  .details-band .row { display: flex; align-items: center; gap: 10px; }
  .details-band svg { width: 18px; height: 18px; flex: none; }
  .accent-line { position: absolute; left: 0; top: 790px; width: 934px; height: 12px; background: var(--orange); }
  .topics { position: absolute; left: 60px; top: 832px; width: 388px; }
  .topic { margin-bottom: 22px; }
  .topic h2 { font-weight: 400; font-size: 17px; line-height: 22px; }
  .topic p { font-size: 15.5px; line-height: 23px; text-align: justify; letter-spacing: 0.3px; }
  .contact { position: absolute; left: 549px; top: 835px; font-size: 17px; line-height: 24px; }
  .contact .row { display: flex; align-items: center; gap: 6px; }
  .contact svg { width: 15px; height: 15px; }
  .partners { position: absolute; left: 549px; top: 1070px; width: 350px; display: flex; justify-content: space-between; align-items: center; }
  .partner { display: flex; align-items: center; gap: 6px; font-size: 16px; line-height: 18px; }
  .partner--primary { color: var(--orange); }
  .partner--alliance { color: var(--blue); }
  .partner .dot { width: 14px; height: 14px; border-radius: 50%; flex: none; }
  .partner--primary .dot { background: var(--orange); }
  .partner--alliance .dot { background: var(--pink); }
</style>
</head>
<body>
<main class="flyer">
  <div class="top-band"></div>

  <svg class="photo-strip" width="934" height="262" viewBox="0 0 934 262">
    <defs>
      <linearGradient id="warm" x1="0" y1="0" x2="1" y2="1"><stop offset="0" stop-color="#d9c7b6"/><stop offset="1" stop-color="#7a5e4c"/></linearGradient>
      <linearGradient id="green" x1="0" y1="0" x2="1" y2="1"><stop offset="0" stop-color="#8fae62"/><stop offset="1" stop-color="#5d5f52"/></linearGradient>
      <linearGradient id="grey" x1="0" y1="0" x2="1" y2="1"><stop offset="0" stop-color="#dedad8"/><stop offset="1" stop-color="#8a6a5a"/></linearGradient>
    </defs>
    <polygon role="img" aria-label="Photo of a smiling young man in glasses pointing forward" points="0,0 320,0 250,262 0,262" fill="url(#warm)"/>
    <polygon role="img" aria-label="Photo of two teenagers studying papers together outdoors" points="338,0 688,0 632,262 268,262" fill="url(#green)"/>
    <polygon role="img" aria-label="Photo of a smiling young woman holding a piggy bank with money" points="708,0 934,0 934,262 600,262" fill="url(#grey)"/>
  </svg>

  <div class="divider divider--pink"></div>
  <div class="divider divider--blue"></div>

  <section class="title-band">
    <h1 class="title">H.E.A.R.T. talk for TEENS</h1>
    <p class="subtitle">Workshops for High School students on<br>HEALTHY EMOTIONS &amp; ATTITUDES in RELATIONSHIPS</p>
  </section>

  <section class="details-band">
    <p>Workshops will be held every Wednesday for 10 weeks starting January 10th.</p>
    <p class="row"><svg viewBox="0 0 20 20"><circle cx="10" cy="11" r="7.5" fill="none" stroke="#fff" stroke-width="2"/><path d="M10 7v4.5h3" fill="none" stroke="#fff" stroke-width="2"/><path d="M2 5l3-3M18 5l-3-3" stroke="#fff" stroke-width="2"/></svg>From 5:30pm—7:30pm</p>
    <p class="row"><svg viewBox="0 0 20 20"><path d="M10 1a6 6 0 0 0-6 6c0 5 6 12 6 12s6-7 6-12a6 6 0 0 0-6-6z" fill="#fff"/><circle cx="10" cy="7" r="2.3" fill="#cc3360"/></svg>Maple Grove Family Resource Center 4180 Willow Bend Road Cedar Ridge, CA 90000</p>
    <p class="row"><svg viewBox="0 0 20 20"><path d="M4 1l3 1 1 4-2 2a11 11 0 0 0 6 6l2-2 4 1 1 3-2 2C9 18 2 11 2 3z" fill="#fff"/></svg>(555) 201-4830 Call to reserve a seat</p>
  </section>
  <div class="accent-line"></div>

  <section class="topics">
    <article class="topic">
      <h2>HEALTHY RELATIONSHIPS WORKSHOPS</h2>
      <p>Topics covered:: self-esteem, recognizing signs of abuse, healthy relationships, safety planning and additional resources.</p>
    </article>
    <article class="topic">
      <h2>FINANCIAL EMPOWERMENT EDUCATION</h2>
      <p>Topics covered: banking, developing a spending plan, understanding &amp; establishing credit, learning hands on tools for money management and much more!</p>
    </article>
    <article class="topic">
      <h2>WORKFORCE READINESS</h2>
      <p>Topics covered: time management, resume building, interview skills, job search experience and much more!</p>
    </article>
  </section>

  <section class="contact">
    <p>For more information call:</p>
    <p>Rosalind Vega, CR-SPH Program Coordinator</p>
    <p class="row"><svg viewBox="0 0 16 16"><rect x="4" y="1" width="8" height="14" rx="1.5" fill="none" stroke="#231f20" stroke-width="1.5"/><line x1="7" y1="12.5" x2="9" y2="12.5" stroke="#231f20" stroke-width="1.5"/></svg>555-318-2746</p>
    <p class="row"><svg viewBox="0 0 16 16"><rect x="1" y="3" width="14" height="10" fill="none" stroke="#231f20" stroke-width="1.5"/><path d="M1 3l7 6 7-6M1 13l5-5M15 13l-5-5" fill="none" stroke="#231f20" stroke-width="1.2"/></svg>rvega@cedarridgeinit.org</p>
  </section>

  <footer class="partners">
    <div class="partner partner--primary"><span class="dot"></span><span>Parejas y Hogares Fuertes</span></div>
    <div class="partner partner--alliance"><span class="dot"></span><span>Cedar Ridge<br>Community Alliance</span></div>
  </footer>
</main>
</body>
</html>
```